PostCard for Managed IT Services

We need a postcard design for a postcard that we intend to send out early in our marketing efforts to medical practices. The postcard should communicate our core services for small businesses including 1.) Managed IT Services, 2.) Security Services, 3.) Cloud Services, and 4.) IT Project and Integration work. company information is available at www.ferndaleit.com. I attached a two logos.WHILE WE WANT TO USE THE LOGO AND COLORS FROM OUR SITE, I HOPE THE DESIGN IS BOLD AND GRABS ATTENTION. I HOPE IT IS NOT THE 'SAME OLD' INFORMATION TECHNOLOGY LOOK. BE CREATIVE AND GET THE READER TO LOOK TWICE.

Target Market(s)

Businesses, medical practices

Font styles to use
Serif
Sans Serif

Requirements
Must have
• We need to include somewhere that are technicians are trained in on HIPAA and PCI (see site for info on the two)

```html
<!DOCTYPE html>
<html lang="en">
<head>
<meta charset="utf-8">
<title>Ferndale IT Postcard</title>
<link href="https://fonts.googleapis.com/css2?family=Open+Sans:wght@300;400;600;700&family=Pathway+Gothic+One&display=swap" rel="stylesheet">
<style>
  :root {
    --navy: #24408a;
    --navy-deep: #1c3272;
    --grey: #a7a8ab;
    --paper: #f2f2f3;
    --white: #ffffff;
    --ink: #2b2b2b;
    --page: #e6e4e1;
  }
  * { margin: 0; padding: 0; box-sizing: border-box; }
  html, body { width: 880px; height: 1200px; overflow: hidden; }
  body { background: var(--page); font-family: "Open Sans", sans-serif; position: relative; }

  .card { position: absolute; left: 56px; width: 771px; height: 518px; overflow: hidden; background: var(--white); box-shadow: 0 3px 10px rgba(0,0,0,.25); }
  .card--front { top: 58px; background: var(--paper); }
  .card--back { top: 629px; }
  .card svg.art { position: absolute; left: 0; top: 0; }

  .brand { position: absolute; text-align: center; color: var(--navy); font-family: "Open Sans", sans-serif; font-weight: 600; }
  .brand__name { font-size: 15px; letter-spacing: 7px; }
  .brand__tag { font-size: 7px; letter-spacing: 4px; margin-top: 4px; }
  .card--front .brand { left: 60px; top: 60px; width: 210px; }
  .card--front .brand__tag--first { margin-top: 52px; }
  .card--back .brand { left: 0; top: 64px; width: 212px; }

  .core { position: absolute; left: 0; top: 163px; width: 420px; height: 175px; background: var(--navy); color: var(--white); padding: 14px 0 0 26px; }
  .core__title { font-family: "Pathway Gothic One", sans-serif; font-weight: 400; font-size: 30px; line-height: 1; letter-spacing: .3px; margin-bottom: 6px; }
  .core__list { list-style: none; }
  .core__list li { display: flex; align-items: center; font-size: 16.5px; font-weight: 300; height: 30.5px; letter-spacing: .3px; }
  .core__list svg { width: 18px; height: 14px; margin: 0 14px 0 8px; }

  .footer-bar { position: absolute; left: 0; top: 460px; width: 771px; height: 58px; background: var(--grey); color: var(--white); display: flex; align-items: center; }
  .footer-bar__text { font-family: "Pathway Gothic One", sans-serif; font-size: 21px; margin-left: 27px; letter-spacing: .3px; }
  .footer-bar__send { margin-left: 54px; width: 26px; height: 22px; }
  .footer-bar__url { font-size: 23px; margin-left: 16px; letter-spacing: .3px; }

  .intro { position: absolute; left: 17px; top: 150px; width: 372px; color: var(--white); }
  .intro__title { font-family: "Pathway Gothic One", sans-serif; font-weight: 400; font-size: 35px; line-height: 1; }
  .intro__lead { font-size: 18px; font-weight: 400; margin-top: 4px; letter-spacing: .2px; }
  .intro__body { font-size: 12.4px; font-weight: 300; line-height: 16.5px; margin-top: 8px; }
  .intro__body + .intro__body { margin-top: 16px; }

  .compliance { position: absolute; left: 17px; top: 383px; font-size: 14px; color: var(--ink); }
  .phone-pill { position: absolute; left: 20px; top: 419px; width: 280px; height: 39px; border-radius: 20px; background: var(--navy); color: var(--white); display: flex; align-items: center; }
  .phone-pill svg { width: 28px; height: 28px; margin: 0 14px 0 28px; }
  .phone-pill__number { font-weight: 700; font-size: 21px; letter-spacing: 1.5px; }
  .contact-line { position: absolute; left: 17px; top: 470px; font-size: 12.5px; color: var(--white); letter-spacing: .3px; }

  .mail-to { position: absolute; left: 422px; top: 28px; color: var(--ink); font-size: 14px; line-height: 20px; }
  .mail-to__name { color: var(--navy); font-size: 16px; margin-bottom: 1px; }
  .stamp-box { position: absolute; left: 647px; top: 26px; width: 106px; height: 70px; border: 1px solid #c9c9cc; }
  .address-line { position: absolute; left: 484px; width: 269px; height: 1px; background: #c9c9cc; }
</style>
</head>
<body>

<section class="card card--front" aria-label="Postcard front">
  <div class="brand">
    <div class="brand__name">FERNDALE IT</div>
    <div class="brand__tag brand__tag--first">MANAGED SERVICES</div>
    <div class="brand__tag">PARTNER WITH THE BEST!</div>
  </div>

  <div class="core">
    <h2 class="core__title">OUR CORE SERVICES</h2>
    <ul class="core__list">
      <li><svg viewBox="0 0 18 14"><path d="M1 7 L6.5 12 L17 1.5" fill="none" stroke="#fff" stroke-width="2.6"/></svg>MANAGED IT SERVICES</li>
      <li><svg viewBox="0 0 18 14"><path d="M1 7 L6.5 12 L17 1.5" fill="none" stroke="#fff" stroke-width="2.6"/></svg>SECURITY SERVICES</li>
      <li><svg viewBox="0 0 18 14"><path d="M1 7 L6.5 12 L17 1.5" fill="none" stroke="#fff" stroke-width="2.6"/></svg>CLOUD SERVICES</li>
      <li><svg viewBox="0 0 18 14"><path d="M1 7 L6.5 12 L17 1.5" fill="none" stroke="#fff" stroke-width="2.6"/></svg>IT PROJECT AND INTEGRATION</li>
    </ul>
  </div>

  <svg class="art" width="771" height="518" viewBox="0 0 771 518">
    <defs>
      <radialGradient id="heroTone" cx="45%" cy="45%" r="65%">
        <stop offset="0" stop-color="#cfe6f4"/>
        <stop offset=".45" stop-color="#5b87a8"/>
        <stop offset="1" stop-color="#1d2430"/>
      </radialGradient>
      <radialGradient id="peopleTone" cx="50%" cy="40%" r="60%">
        <stop offset="0" stop-color="#d9e4ec"/><stop offset="1" stop-color="#6f8798"/>
      </radialGradient>
      <radialGradient id="lockTone" cx="50%" cy="45%" r="60%">
        <stop offset="0" stop-color="#4c8de0"/><stop offset="1" stop-color="#0c2a78"/>
      </radialGradient>
      <radialGradient id="cloudTone" cx="50%" cy="45%" r="60%">
        <stop offset="0" stop-color="#3d5d9c"/><stop offset="1" stop-color="#0f1f4a"/>
      </radialGradient>
    </defs>
    <circle cx="660" cy="232" r="312" fill="#fff"/>
    <circle cx="668" cy="236" r="308" fill="none" stroke="var(--navy)" stroke-width="2"/>
    <circle cx="662" cy="232" r="302" fill="none" stroke="var(--navy)" stroke-width="2.5"/>
    <circle cx="653" cy="232" r="294" fill="url(#heroTone)" role="img" aria-label="Photo of a businessman holding a glowing globe linked to devices"/>

    <circle cx="79" cy="398" r="52" fill="#fff" stroke="var(--navy)" stroke-width="3"/>
    <circle cx="79" cy="398" r="47" fill="url(#peopleTone)" role="img" aria-label="Photo of business figures on a connected network floor"/>
    <circle cx="191" cy="398" r="52" fill="#fff" stroke="var(--navy)" stroke-width="3"/>
    <circle cx="191" cy="398" r="47" fill="url(#lockTone)" role="img" aria-label="Photo of a digital padlock over data"/>
    <circle cx="303" cy="398" r="52" fill="#fff" stroke="var(--navy)" stroke-width="3"/>
    <circle cx="303" cy="398" r="47" fill="url(#cloudTone)" role="img" aria-label="Photo of a hand drawing a cloud network diagram"/>
  </svg>

  <div class="footer-bar">
    <span class="footer-bar__text">FOR MORE INFORMATION PLEASE CONTACT US</span>
    <svg class="footer-bar__send" viewBox="0 0 26 22"><path d="M1 3 L25 11 L9 21 L10 13 Z M10 13 L25 11" fill="#fff" stroke="#fff" stroke-width="1" stroke-linejoin="round"/><path d="M10 13 L25 11" stroke="var(--grey)" stroke-width="1.5"/></svg>
    <span class="footer-bar__url">www.ferndaleit.com</span>
  </div>
</section>

<section class="card card--back" aria-label="Postcard back">
  <svg class="art" width="771" height="518" viewBox="0 0 771 518">
    <defs>
      <clipPath id="panelClip"><circle cx="153" cy="258" r="273"/></clipPath>
      <linearGradient id="bandTone" x1="0" y1="0" x2="1" y2="1">
        <stop offset="0" stop-color="#2a4893"/><stop offset="1" stop-color="var(--navy-deep)"/>
      </linearGradient>
    </defs>
    <g clip-path="url(#panelClip)">
      <rect x="0" y="0" width="771" height="518" fill="var(--paper)"/>
      <rect x="0" y="140" width="771" height="236" fill="url(#bandTone)"/>
      <rect x="0" y="439" width="771" height="79" fill="var(--grey)"/>
    </g>
    <circle cx="153" cy="258" r="273" fill="none" stroke="#fff" stroke-width="6"/>
    <circle cx="158" cy="262" r="280" fill="none" stroke="var(--navy)" stroke-width="2"/>
    <circle cx="150" cy="258" r="286" fill="none" stroke="var(--navy)" stroke-width="2.5"/>
  </svg>

  <div class="brand">
    <div class="brand__name">FERNDALE IT</div>
  </div>

  <div class="intro">
    <h1 class="intro__title">FERNDALE MANAGED SERVICES</h1>
    <p class="intro__lead">Partner with the best for all your IT needs!</p>
    <p class="intro__body">We are committed to being the leading Managed IT Service Provider. We are located in Marlow, ND and we serve clients nation wide! We have and serve clients in every industry. Your data and network need to be secure in today’s world and we do our best to ensure that it is.</p>
    <p class="intro__body">At Ferndale IT, our goal is to provide the best IT solution for your business while keeping your IT costs down.</p>
  </div>

  <p class="compliance">Our technicians are trained in on HIPAA and PCI</p>

  <div class="phone-pill">
    <svg viewBox="0 0 28 28"><circle cx="15" cy="13" r="10" fill="none" stroke="#fff" stroke-width="2"/><path d="M3 14 C3 22 10 26 16 26 L14 23 C10 23 6 20 6 14 Z" fill="#fff"/><text x="15" y="16.5" font-family="Open Sans, sans-serif" font-size="9" font-weight="700" fill="#fff" text-anchor="middle">24</text></svg>
    <span class="phone-pill__number">(555) 014-2870</span>
  </div>

  <p class="contact-line">www.ferndaleit.com | info@ferndaleit.com</p>

  <address class="mail-to" style="font-style:normal">
    <div class="mail-to__name">Ferndale IT</div>
    1180 Alder Street East<br>
    Suite 305 Marlow, ND 58000
  </address>
  <div class="stamp-box"></div>
  <div class="address-line" style="top:195px"></div>
  <div class="address-line" style="top:244px"></div>
  <div class="address-line" style="top:293px"></div>
  <div class="address-line" style="top:340px"></div>
</section>

</body>
</html>
```